Redesign of an insurance website

Attached is an insurance website that I need to redesign. Currently the website is too dark. I like for example www.brenvalo.com . Could you make the website lighter and change the structure a little so that it is more user friendly?

Industry/Entity Type

Insurance

Number of Pages Required

4 page

```html
<!DOCTYPE html>
<html lang="cs">
<head>
<meta charset="utf-8">
<title>Jistapolisa.cz</title>
<link href="https://fonts.googleapis.com/css2?family=Open+Sans:wght@300;400;600;700&display=swap" rel="stylesheet">
<style>
:root{
  --blue:#0055a5;
  --orange:#f07f1f;
  --ink:#1b1b1b;
  --text:#333;
  --muted:#8a8a8a;
  --line:#cfcfcf;
  --band-light:#f5f5f5;
  --band-mid:#ececec;
  --band-dark:#cfcfcf;
  --white:#fff;
}
*{box-sizing:border-box;margin:0;padding:0}
html,body{width:1018px;height:1200px;overflow:hidden}
body{font-family:"Open Sans",Arial,sans-serif;color:var(--text);background:var(--white);position:relative}
.abs{position:absolute}
/* header */
.site-header{position:absolute;left:0;top:0;width:1018px;height:65px;background:var(--blue);color:var(--white)}
.main-nav{position:absolute;left:38px;top:23px;display:flex;gap:16px;font-size:11px;font-weight:600}
.brand{position:absolute;left:0;width:1018px;top:20px;text-align:center;font-size:18px;font-weight:700;letter-spacing:.5px}
.btn-register{position:absolute;left:789px;top:21px;width:88px;height:21px;border:1px solid var(--white);font-size:8px;font-weight:700;display:flex;align-items:center;justify-content:center}
.login{position:absolute;left:902px;top:24px;font-size:11px;font-weight:600}
.avatar{position:absolute;left:970px;top:23px;width:18px;height:18px;border-radius:50%;background:#9dbbe3}
/* hero */
h2.section-title{font-size:15px;font-weight:600;color:var(--ink);position:absolute}
.type-item{position:absolute;left:125px;width:150px;height:50px}
.type-icon{position:absolute;left:0;top:0;width:50px;height:50px;border-radius:50%;border:1.5px solid #9a9a9a;display:flex;align-items:center;justify-content:center}
.type-item.active .type-icon{background:var(--orange);border-color:var(--orange)}
.type-label{position:absolute;left:82px;top:11px;font-size:10.5px;font-weight:600;color:#8a8a8a;line-height:14px}
.feature-circle{position:absolute;left:349px;top:192px;width:236px;height:236px;border-radius:50%;background:var(--blue)}
.feature-label{position:absolute;left:0;width:236px;top:162px;text-align:center;color:var(--white);font-size:12.5px;font-weight:600}
.check-badge{position:absolute;left:528px;top:208px;width:46px;height:46px;border-radius:50%;background:var(--orange);border:3px solid var(--white);display:flex;align-items:center;justify-content:center}
.field{position:absolute;left:649px;width:244px;height:40px;border:1.5px solid #dcdcdc;font-size:12px;color:#999;padding:11px 15px}
.agree{position:absolute;left:649px;top:347px;font-size:11px;color:var(--text);display:flex;align-items:center;gap:13px}
.agree .box{width:14px;height:14px;border:1px solid #ccc;display:flex;align-items:center;justify-content:center}
.agree .box i{width:6px;height:6px;background:var(--orange)}
.agree u{text-decoration:underline}
.btn-price{position:absolute;left:648px;top:387px;width:163px;height:37px;background:var(--orange);color:var(--white);font-size:14px;font-weight:700;display:flex;align-items:center;justify-content:center;letter-spacing:.3px}
/* benefits */
.benefits{position:absolute;left:0;top:488px;width:1018px;height:256px;background:var(--band-light)}
.benefits h2{position:absolute;left:0;width:1018px;top:49px;text-align:center;font-size:15px;font-weight:600;color:var(--ink)}
.benefit{position:absolute;font-size:13px;font-weight:300;color:#333;display:flex;align-items:center;gap:22px}
.benefit.light{color:var(--muted)}
/* articles */
.articles{position:absolute;left:0;top:744px;width:1018px;height:256px;background:var(--band-mid)}
.review-photo{position:absolute;left:125px;top:32px;width:221px;height:192px;border-radius:10px;background:radial-gradient(circle at 45% 75%,#fdfdfd 0%,#e4e4e4 55%,#b9b9b9 85%,#3a3a3a 100%)}
.article{position:absolute;top:31px}
.article h3{font-size:12.5px;font-weight:600;color:var(--ink);line-height:16px;margin-bottom:10px}
.article p{font-size:9.6px;line-height:15.5px;color:#3a3a3a;letter-spacing:-.15px}
/* newsletter */
.newsletter{position:absolute;left:0;top:1000px;width:1018px;height:73px;background:var(--band-dark);color:var(--white)}
.newsletter .brand-foot{position:absolute;left:125px;top:25px;font-size:18px;font-weight:700}
.newsletter .nl-label{position:absolute;left:390px;top:28px;font-size:12px;font-weight:600;letter-spacing:.3px}
.nl-input{position:absolute;left:559px;top:22px;width:221px;height:29px;background:#dcdcdc;font-size:9px;color:#f3f3f3;padding:9px 12px}
.nl-btn{position:absolute;left:780px;top:22px;width:114px;height:29px;background:var(--white);color:var(--orange);font-size:10px;font-weight:600;display:flex;align-items:center;justify-content:center;letter-spacing:.6px}
/* footer */
.legal{position:absolute;left:125px;top:1119px;font-size:10px;color:#666;line-height:20px}
.join{position:absolute;left:668px;top:1126px;font-size:11px;font-weight:600;color:#333}
.social{position:absolute;top:1120px;width:28px;height:28px;border-radius:50%;border:2px solid #555}
</style>
</head>
<body>
<header class="site-header">
  <nav class="main-nav"><span>O Nas</span><span>Caste Dotazy</span><span>Kontakt</span></nav>
  <div class="brand">JISTAPOLISA.CZ</div>
  <div class="btn-register">RGISTROVAT</div>
  <div class="login">Prihlasit se</div>
  <div class="avatar"></div>
</header>

<main>
  <h2 class="section-title" style="left:124px;top:121px">Chcete pojistit neco jineho?</h2>
  <h2 class="section-title" style="left:642px;top:123px">Najdete nejvyhodnejsi pojisteni</h2>

  <svg class="abs" style="left:141px;top:176px" width="18" height="12" viewBox="0 0 18 12"><path d="M1 10 9 2l8 8" fill="none" stroke="#999" stroke-width="1.5"/></svg>

  <div class="type-item active" style="top:199px">
    <div class="type-icon"><svg width="30" height="16" viewBox="0 0 30 16"><path d="M2 12c0-3 3-4 6-4l4-5h8l5 5c2 0 3 2 3 4z" fill="#fff"/><circle cx="9" cy="12" r="2.5" fill="#f07f1f"/><circle cx="21" cy="12" r="2.5" fill="#f07f1f"/></svg></div>
    <div class="type-label">Havarijni<br>Pojisteni</div>
  </div>
  <div class="type-item" style="top:257px">
    <div class="type-icon"><svg width="22" height="22" viewBox="0 0 22 22"><path d="M4 18 18 4M8 6l9 3M6 12l4 5M3 16l3 3" fill="none" stroke="#888" stroke-width="2" stroke-linecap="round"/></svg></div>
    <div class="type-label">Cestovani<br>Pojisteni</div>
  </div>
  <div class="type-item" style="top:315px">
    <div class="type-icon"><svg width="22" height="22" viewBox="0 0 22 22"><path d="M3 11 11 3l8 8M5 9v10h12V9" fill="none" stroke="#888" stroke-width="1.8"/></svg></div>
    <div class="type-label">Pojisteni<br>Domova</div>
  </div>
  <div class="type-item" style="top:373px">
    <div class="type-icon"><svg width="24" height="20" viewBox="0 0 24 20"><path d="M3 15V11l3-5h12l3 5v4zM9 6V3h6v3" fill="none" stroke="#888" stroke-width="1.6"/><circle cx="7" cy="15" r="2" fill="none" stroke="#888" stroke-width="1.6"/><circle cx="17" cy="15" r="2" fill="none" stroke="#888" stroke-width="1.6"/></svg></div>
    <div class="type-label">Povinne<br>Ruceni</div>
  </div>

  <svg class="abs" style="left:141px;top:437px" width="18" height="12" viewBox="0 0 18 12"><path d="M1 2l8 8 8-8" fill="none" stroke="#f07f1f" stroke-width="1.8"/></svg>

  <div class="feature-circle">
    <svg class="abs" style="left:38px;top:78px" width="164" height="70" viewBox="0 0 164 70"><path d="M6 52c0-10 10-14 22-16 8-14 18-26 38-26h22c20 0 32 12 42 26 14 0 28 4 28 16z" fill="#fff"/><path d="M62 18h18v18H54c2-8 4-14 8-18zM88 18c10 0 18 8 22 18H88z" fill="#0055a5"/><circle cx="36" cy="52" r="13" fill="#fff"/><circle cx="36" cy="52" r="9" fill="#0055a5"/><circle cx="126" cy="52" r="13" fill="#fff"/><circle cx="126" cy="52" r="9" fill="#0055a5"/></svg>
    <div class="feature-label">Havarijni Pojisteni</div>
  </div>
  <div class="check-badge"><svg width="20" height="16" viewBox="0 0 20 16"><path d="M2 8l6 5 10-11" fill="none" stroke="#fff" stroke-width="3"/></svg></div>

  <div class="field" style="top:198px">Jmeno</div>
  <div class="field" style="top:246px">Prijment</div>
  <div class="field" style="top:294px">E-mail</div>
  <div class="agree"><span class="box"><i></i></span><span>Souhlasim s <u>podminkami pouziti</u></span></div>
  <div class="btn-price">SPOCITAT CENU</div>
</main>

<section class="benefits">
  <h2>Proc hledat pojisteni pres Jistapolisa.cz?</h2>
  <div class="benefit" style="left:217px;top:100px"><svg width="16" height="15" viewBox="0 0 16 15"><path d="M8 1l2 5h5l-4 3 1.6 5L8 11l-4.6 3L5 9 1 6h5z" fill="none" stroke="#f07f1f" stroke-width="1.3"/></svg>S nami najdete tu nejvyhodnejsi nabidku</div>
  <div class="benefit" style="left:217px;top:129px"><svg width="16" height="15" viewBox="0 0 16 15"><path d="M8 1l2 5h5l-4 3 1.6 5L8 11l-4.6 3L5 9 1 6h5z" fill="none" stroke="#f07f1f" stroke-width="1.3"/></svg>zarucime vam nejlepsi cenu na trhu</div>
  <div class="benefit" style="left:217px;top:158px"><svg width="16" height="15" viewBox="0 0 16 15"><path d="M8 1l2 5h5l-4 3 1.6 5L8 11l-4.6 3L5 9 1 6h5z" fill="none" stroke="#f07f1f" stroke-width="1.3"/></svg>staci par minut a muzete usetrit tisice</div>
  <div class="benefit" style="left:217px;top:187px"><svg width="16" height="15" viewBox="0 0 16 15"><path d="M8 1l2 5h5l-4 3 1.6 5L8 11l-4.6 3L5 9 1 6h5z" fill="none" stroke="#f07f1f" stroke-width="1.3"/></svg>srovnavame vsechny pojistovny</div>
  <div class="benefit light" style="left:537px;top:100px"><svg width="16" height="15" viewBox="0 0 16 15"><path d="M8 1l2 5h5l-4 3 1.6 5L8 11l-4.6 3L5 9 1 6h5z" fill="none" stroke="#f07f1f" stroke-width="1.3"/></svg>zridime vam vsechny druhy pojisteni</div>
  <div class="benefit light" style="left:537px;top:129px"><svg width="16" height="15" viewBox="0 0 16 15"><path d="M8 1l2 5h5l-4 3 1.6 5L8 11l-4.6 3L5 9 1 6h5z" fill="none" stroke="#f07f1f" stroke-width="1.3"/></svg>vse vyridite z pohodli domova</div>
  <div class="benefit light" style="left:537px;top:158px"><svg width="16" height="15" viewBox="0 0 16 15"><path d="M8 1l2 5h5l-4 3 1.6 5L8 11l-4.6 3L5 9 1 6h5z" fill="none" stroke="#f07f1f" stroke-width="1.3"/></svg>nemusite nikam chodit a usetrite</div>
</section>

<section class="articles">
  <div class="review-photo" role="img" aria-label="Photo of a clock face with the words Time for review"></div>
  <article class="article" style="left:390px;width:252px">
    <h3>Uxavreli jste v minulosti nevyhodnou pojistku? Zbavte se ji!</h3>
    <p>Lorem Ipsum is simply dummy text of the printing and typesetting industry. Lorem Ipsum has been the industry's standard dummy text ever since the 1500s, when an unknown printer took a galley of type and scrambled it to make a type specimen book. It has survived not only five centuries, but also the leap into electronic typesetting, remaining essentially unchanged. It was popularised in the 1960s with the release including versions of Lorem Ipsum.</p>
  </article>
  <article class="article" style="left:669px;width:225px">
    <h3>Jak to fungule</h3>
    <p style="margin-top:16px">Lorem Ipsum is simply dummy text of the printing and typesetting industry. Lorem Ipsum has been the industry's standard dummy text ever since the 1500s, when an unknown printer took a galley of type and scrambled it to make a type specimen book. It has survived not only five centuries, but also the leap into electronic typesetting, remaining essentially unchanged.</p>
  </article>
</section>

<section class="newsletter">
  <div class="brand-foot">JISTAPOLISA.CZ</div>
  <div class="nl-label">ODEBIRAT NEWSLETTER</div>
  <div class="nl-input">E-mail</div>
  <div class="nl-btn">POTVRDIT</div>
</section>

<footer>
  <div class="legal">Ochrana Soukromi &nbsp;|&nbsp; Podminky Pouziti<br>© Copyright 2017 Jistapolisa.cz. Vsechna prava vyhrazena.</div>
  <div class="join">Join us on</div>
  <div class="social" style="left:742px" aria-label="Social link"></div>
  <div class="social" style="left:783px" aria-label="Social link"></div>
  <div class="social" style="left:824px" aria-label="Social link"></div>
  <div class="social" style="left:865px" aria-label="Social link"></div>
</footer>
</body>
</html>
```